KORBALT

The business want a professional looking business card. We have a scetch we will add but want the extra upgrade, and would like more suggestions for variations of our business cards.

```html
<!DOCTYPE html>
<html lang="en">
<head>
<meta charset="utf-8">
<title>KORBALT Business Card</title>
<link href="https://fonts.googleapis.com/css2?family=Montserrat:wght@400;500;600&family=Playfair+Display:wght@700&display=swap" rel="stylesheet">
<style>
  :root {
    --backdrop: #808080;
    --card-white: #ffffff;
    --brown: #704a1d;
    --brown-text: #6b4518;
    --gold: #e6c069;
    --gold-light: #fdd77a;
    --gold-dark: #c9a14e;
  }
  * { margin: 0; padding: 0; box-sizing: border-box; }
  html, body { width: 1200px; height: 1027px; overflow: hidden; background: var(--backdrop); }
  .canvas { position: relative; width: 1200px; height: 1027px; }

  .card { position: absolute; left: 260px; width: 679px; height: 397px; overflow: hidden; }
  .card-front { top: 87px; background: var(--card-white); }
  .card-back { top: 542px; background: var(--brown); }

  .wave { position: absolute; left: 0; top: 0; width: 679px; height: 397px; }

  .divider {
    position: absolute; left: 275px; top: 29px; width: 2px; height: 264px;
    background: linear-gradient(to bottom, transparent, var(--gold-light) 15%, var(--gold-light) 85%, transparent);
  }

  .brand-block { position: absolute; left: 39px; top: 158px; width: 220px; text-align: center; }
  .brand-name {
    font-family: "Playfair Display", Georgia, serif; font-weight: 700;
    font-size: 37px; line-height: 1; color: var(--brown-text); letter-spacing: 1px;
  }
  .brand-since {
    margin-top: 4px; font-family: "Montserrat", Arial, sans-serif; font-weight: 600;
    font-size: 8.5px; letter-spacing: 3.5px; color: var(--gold-dark);
  }

  .person { position: absolute; left: 315px; top: 58px; }
  .person-company {
    font-family: "Playfair Display", Georgia, serif; font-weight: 700;
    font-size: 28px; line-height: 1; color: var(--brown-text); white-space: nowrap;
  }
  .person-title {
    margin-top: 16px; font-family: "Montserrat", Arial, sans-serif; font-weight: 400;
    font-size: 21px; line-height: 1; color: var(--brown-text);
  }
  .person-name {
    margin-top: 3px; font-family: "Montserrat", Arial, sans-serif; font-weight: 500;
    font-size: 13px; line-height: 1; color: var(--brown-text);
  }

  .contact-list { position: absolute; left: 315px; top: 183px; list-style: none; }
  .contact-item { display: flex; align-items: center; height: 22px; margin-bottom: 9.5px; }
  .contact-icon {
    width: 22px; height: 22px; border-radius: 4px; background: var(--brown);
    display: flex; align-items: center; justify-content: center; margin-right: 12px;
  }
  .contact-text {
    font-family: "Montserrat", Arial, sans-serif; font-weight: 400;
    font-size: 19px; color: var(--brown-text); line-height: 1;
  }

  .back-name {
    position: absolute; left: 0; right: 0; top: 160px; text-align: center;
    font-family: "Playfair Display", Georgia, serif; font-weight: 700;
    font-size: 54px; line-height: 1; color: var(--gold); letter-spacing: 1px;
  }
</style>
</head>
<body>
<main class="canvas">

  <section class="card card-front">
    <svg class="wave" viewBox="0 0 679 397" aria-hidden="true">
      <defs>
        <linearGradient id="goldBand" x1="0" y1="0" x2="1" y2="0">
          <stop offset="0" stop-color="#c9a14e"/>
          <stop offset="0.1" stop-color="#fdd77a"/>
          <stop offset="0.25" stop-color="#f7dc96"/>
          <stop offset="0.38" stop-color="#fdd77a"/>
          <stop offset="0.46" stop-color="#c9a14e"/>
          <stop offset="0.58" stop-color="#fdd77a"/>
          <stop offset="0.75" stop-color="#f7dc96"/>
          <stop offset="0.88" stop-color="#c9a14e"/>
          <stop offset="1" stop-color="#fdd77a"/>
        </linearGradient>
      </defs>
      <path class="wave-gold" fill="url(#goldBand)"
        d="M0 246 C80 320 170 350 290 340 C370 333 420 310 500 314 C580 316 640 330 679 348 L679 365 C640 345 580 338 504 339 C420 340 370 360 290 367 C180 376 60 365 0 306 Z"/>
      <path class="wave-brown" fill="#704a1d"
        d="M0 306 C60 365 180 376 290 367 C370 360 420 340 504 339 C580 338 640 345 679 365 V397 H0 Z"/>
    </svg>

    <div class="brand-block">
      <div class="brand-name">KORBALT</div>
      <div class="brand-since">SINCE 2026</div>
    </div>

    <div class="divider"></div>

    <div class="person">
      <div class="person-company">KORBALT HALVORSEN</div>
      <div class="person-title">CEO &amp; Founder</div>
      <div class="person-name">Lars Erik Halvorsen</div>
    </div>

    <ul class="contact-list">
      <li class="contact-item">
        <span class="contact-icon">
          <svg width="13" height="13" viewBox="0 0 24 24" aria-hidden="true"><path fill="#fff" d="M6.6 10.8a15.1 15.1 0 0 0 6.6 6.6l2.2-2.2c.3-.3.7-.4 1-.2 1.1.4 2.3.6 3.6.6.6 0 1 .4 1 1V20c0 .6-.4 1-1 1A17 17 0 0 1 3 4c0-.6.4-1 1-1h3.5c.6 0 1 .4 1 1 0 1.3.2 2.5.6 3.6.1.3 0 .7-.2 1z"/></svg>
        </span>
        <span class="contact-text">004791234560</span>
      </li>
      <li class="contact-item">
        <span class="contact-icon">
          <svg width="13" height="10" viewBox="0 0 26 20" aria-hidden="true"><rect x="1.5" y="1.5" width="23" height="17" rx="1.5" fill="none" stroke="#fff" stroke-width="2.4"/><path d="M2 3l11 8 11-8" fill="none" stroke="#fff" stroke-width="2.4"/></svg>
        </span>
        <span class="contact-text">korbalt.llc@postmail.com</span>
      </li>
      <li class="contact-item">
        <span class="contact-icon">
          <svg width="14" height="14" viewBox="0 0 24 24" aria-hidden="true" fill="none" stroke="#fff" stroke-width="2"><circle cx="12" cy="12" r="10"/><ellipse cx="12" cy="12" rx="4.5" ry="10"/><path d="M2 12h20"/></svg>
        </span>
        <span class="contact-text">www.korbalt.llc</span>
      </li>
    </ul>
  </section>

  <section class="card card-back">
    <div class="back-name">KORBALT</div>
  </section>

</main>
</body>
</html>
```